Business Card Needed for Crafter of Pottery, Jewelry and Artwork

Calling all designers in search of an artistic challenge.

I need a new business card design for my pottery, jewelry and artwork business, Woven Glass and Tide, based in Vancouver BC.

I would like a card that is bright and inviting and preferably incorporates my logo and a sample of photos of my work while having a clean fresh look. The following contact details would preferably be included on the card as well:
• Helena Pikeworth
• Designer
• Phone: 604.555.0172
• Email: Designer@WovenGlassandTide.example
• Website: www.WovenGlassandTide.example
• Blog: www.ShapingHillside.example

The logo is attached in two color schemes in both Vector and Source formats. On past cards I’ve also included photos of my work. By including photos of the work the pieces are showcased and it catches people’s eye and prompts them to pick up the card and look at it more closely. For example, if I leave a stack in a coffee shop I want people to be drawn to the card, to pick it up and get a sense of the my product lines. Please feel free to pull photos of my work directly off of my website. If you need photos with higher pixels please let me know and I’ll email them directly to you. The website background is bffbda (191, 251, 218). I would like the business cards to match the feel of the website for consistency but the cards do not need to use the exact same colors. My website and current business card are predominantly turquoise shades. The background uses stripes provided by the website template. I don’t know the exact colors of the stripes.

My current business card is attached to show the use of photos in a design. Please note that I am not thrilled with my own design and am looking for variations and completely new designs. This example is not meant to be used as a template or starting point.

Here is some background surrounding my company:
WGT offers one of a kind jewelry, pottery, artwork and leather bags each designed with a twist. The pottery varies from rustic every day functional ware to raku artwork. The jewelry ranges from simple sterling every day pieces to multimedia pieces incorporating stone, metal, ceramics and fabric. The artwork is multimedia, typically acrylic paired with a natural element such as bark. All the bags are leather with reworked kimono fabric or patterned silk lining.

Feel free to check out my website to get a flavour for my work and the color scheme I've used on marketing materials so far. www.wovenglassandtide.example
Updates

Thank you to everyone who has submitted a design so far. I hope everyone has received some helpful feedback.

I'm going to post a survey to customers and friends asking for their votes. If you have new designs to submit please try to get them in by Saturday March 30 at noon so that I can include it in the survey launch.

Thank you

Target Market(s)

Females aged 25-65 interested in one of a kind functional pottery and jewelry.

Industry/Entity Type

Coffee Shop

Requirements
Must have
• Contact information, website, blog
Nice to have
• Logo, photos

```html
<!DOCTYPE html>
<html lang="en">
<head>
<meta charset="utf-8">
<title>Woven Glass and Tide — Business Card</title>
<link rel="stylesheet" href="https://fonts.googleapis.com/css2?family=Marcellus+SC&family=Marcellus&display=swap">
<style>
  :root {
    --page: #efefef;
    --card: #2e2456;
    --card-light: #ffffff;
    --ink-soft: #d9d6e8;
    --accent: #3bbfad;
    --logo-ink: #2e2456;
    --photo-pottery: #cfd0cb;
    --photo-jewelry: #e6e6ea;
    --photo-linen: #bdbab3;
  }
  * { box-sizing: border-box; margin: 0; padding: 0; }
  html, body { width: 1200px; height: 2807px; overflow: hidden; }
  body {
    background: var(--page);
    font-family: "Marcellus SC", "Marcellus", serif;
    position: relative;
  }
  .card {
    position: absolute;
    left: 100px;
    width: 1000px;
    height: 571px;
    background: var(--card);
    color: var(--card-light);
    overflow: hidden;
    box-shadow: 0 18px 40px rgba(0,0,0,0.18);
  }
  .card--front { top: 752px; }
  .card--back { top: 1483px; }

  .logo-badge {
    position: absolute;
    left: 50%;
    transform: translateX(-50%);
    border-radius: 50%;
    background: var(--card-light);
    border: 8px solid var(--accent);
    display: flex;
    align-items: center;
    justify-content: center;
    text-align: center;
  }
  .logo-badge__name {
    color: var(--logo-ink);
    font-family: "Marcellus SC", serif;
    font-weight: 400;
    line-height: 1.15;
  }
  .card--front .logo-badge { top: 30px; width: 226px; height: 226px; }
  .card--front .logo-badge__name { font-size: 28px; }
  .card--back .logo-badge { top: 300px; width: 236px; height: 236px; }
  .card--back .logo-badge__name { font-size: 30px; }

  .identity {
    position: absolute;
    top: 270px;
    left: 50%;
    transform: translateX(-50%);
    width: 460px;
    text-align: center;
  }
  .identity__name { font-size: 44px; line-height: 54px; letter-spacing: 1.5px; font-weight: 400; white-space: nowrap; }
  .identity__role { font-size: 26px; line-height: 34px; color: var(--ink-soft); margin-top: 2px; letter-spacing: 1px; }

  .contact {
    position: absolute;
    display: flex;
    align-items: center;
    gap: 12px;
    font-size: 20px;
    line-height: 26px;
    letter-spacing: 0.5px;
    color: var(--card-light);
    white-space: nowrap;
  }
  .contact svg { width: 22px; height: 22px; flex: none; }
  .contact--phone { right: 48px; top: 328px; }
  .contact--email { right: 48px; top: 412px; }
  .contact--site  { left: 40px; top: 468px; }
  .contact--blog  { left: 40px; top: 510px; }

  .dots {
    position: absolute;
    display: flex;
    gap: 26px;
  }
  .dots span { width: 7px; height: 7px; border-radius: 50%; background: var(--card-light); }
  .card--front .dots { left: 590px; top: 536px; }
  .card--back .dots { left: 760px; top: 520px; }

  .gallery {
    position: absolute;
    top: 0; left: 0;
    width: 1000px;
    height: 262px;
    display: flex;
  }
  .gallery__tile { height: 100%; }
  .gallery__tile--pottery { width: 300px; background: linear-gradient(160deg, #e3e4e0, var(--photo-pottery) 60%, #b9b7a6); }
  .gallery__tile--jewelry { width: 360px; background: linear-gradient(135deg, #f1f1f4, var(--photo-jewelry) 55%, #cfcdd6); }
  .gallery__tile--linen   { width: 340px; background: linear-gradient(150deg, #cac7c0, var(--photo-linen) 60%, #a8c9c8); }
</style>
</head>
<body>

<section class="card card--front" aria-label="Business card front">
  <div class="logo-badge">
    <span class="logo-badge__name">Woven<br>Glass<br>and Tide</span>
  </div>

  <div class="identity">
    <h1 class="identity__name">Helena Pikeworth</h1>
    <p class="identity__role">Designer</p>
  </div>

  <p class="contact contact--phone">
    <svg viewBox="0 0 24 24" aria-hidden="true"><rect x="6" y="2" width="12" height="20" rx="2" fill="none" stroke="currentColor" stroke-width="2"/><circle cx="12" cy="18" r="1.2" fill="currentColor"/></svg>
    604.555.0172
  </p>
  <p class="contact contact--email">
    <svg viewBox="0 0 24 24" aria-hidden="true"><rect x="2" y="5" width="20" height="14" fill="currentColor"/><path d="M2 5 L12 13 L22 5" fill="none" stroke="#2e2456" stroke-width="1.6"/></svg>
    Designer@WovenGlassandTide.example
  </p>
  <p class="contact contact--site">
    <svg viewBox="0 0 24 24" aria-hidden="true"><circle cx="12" cy="12" r="9.5" fill="none" stroke="currentColor" stroke-width="1.8"/><ellipse cx="12" cy="12" rx="4.2" ry="9.5" fill="none" stroke="currentColor" stroke-width="1.5"/><path d="M2.5 12 H21.5 M4.5 7 H19.5 M4.5 17 H19.5" stroke="currentColor" stroke-width="1.4"/></svg>
    www.WovenGlassandTide.example
  </p>
  <p class="contact contact--blog">
    <svg viewBox="0 0 24 24" aria-hidden="true"><circle cx="12" cy="12" r="9.5" fill="none" stroke="currentColor" stroke-width="1.8"/></svg>
    www.ShapingHillside.example
  </p>

  <div class="dots" aria-hidden="true"><span></span><span></span><span></span></div>
</section>

<section class="card card--back" aria-label="Business card back">
  <div class="gallery">
    <div class="gallery__tile gallery__tile--pottery" role="img" aria-label="Photo of glazed pottery cups"></div>
    <div class="gallery__tile gallery__tile--jewelry" role="img" aria-label="Photo of beaded earrings hanging from a branch"></div>
    <div class="gallery__tile gallery__tile--linen" role="img" aria-label="Photo of turquoise and pink beads on linen"></div>
  </div>

  <div class="logo-badge">
    <span class="logo-badge__name">Woven<br>Glass<br>and Tide</span>
  </div>

  <div class="dots" aria-hidden="true"><span></span><span></span><span></span></div>
</section>

</body>
</html>
```